Multi Academy Trust needs to shout about our vision by turning our words into something that can ...

Our vision is something we want to shout about and share through multiple media avenues to a range of stakeholders including parents, staff, pupils, other school trusts, Council for Civic Standards and suppliers. We want an eye-catching design that stands out from the crowd but incorporates our current brand (and logo)

```html
<!DOCTYPE html>
<html lang="en">
<head>
<meta charset="utf-8">
<title>Harbourline Learning Trust – Our Vision</title>
<link href="https://fonts.googleapis.com/css2?family=Abel&display=swap" rel="stylesheet">
<style>
  :root {
    --blue-dark: #2389cc;
    --blue-light: #62b4e4;
    --blue-text: #2f8fd0;
    --grey-text: #6f6f72;
    --grey-soft: #ececef;
    --white: #ffffff;
    --photo-green: #4a5a3c;
    --photo-navy: #2a3d7a;
  }
  * { margin: 0; padding: 0; box-sizing: border-box; }
  html, body { width: 792px; height: 1200px; overflow: hidden; background: var(--white); }
  body { font-family: "Abel", "Arial Narrow", sans-serif; }
  .flyer { position: relative; width: 792px; height: 1200px; overflow: hidden; background: var(--white); }
  .flyer-shapes { position: absolute; inset: 0; width: 792px; height: 1200px; }

  .brand { position: absolute; left: 24px; top: 28px; display: flex; align-items: center; gap: 12px; }
  .brand-dot { width: 48px; height: 48px; border-radius: 50%; background: var(--blue-dark); }
  .brand-name { color: #58585b; font-size: 26px; line-height: 25px; }

  .tag { position: absolute; height: 26px; font-size: 16px; line-height: 26px; padding: 0 10px; }
  .tag--light { background: var(--white); color: var(--blue-text); text-align: right; }
  .tag--solid { background: var(--blue-dark); color: var(--white); }

  .vision { position: absolute; right: 32px; text-align: right; color: var(--white); }
  .vision-lead { font-size: 14.5px; }
  .vision-copy { font-size: 12px; line-height: 17px; }
  .vision-list { list-style: none; font-size: 12px; line-height: 23px; }

  .photo-question { position: absolute; left: 53px; top: 576px; color: var(--white); font-size: 25px; }

  .pillar-intro { position: absolute; color: var(--blue-text); font-size: 12px; }
  .pillar-list { position: absolute; list-style: none; color: var(--grey-text); font-size: 11.6px; line-height: 23px; }
  .pillar-list--right { text-align: right; right: 38px; width: 330px; }
  .pillar-list--left { left: 34px; width: 372px; }

  .column-rule { position: absolute; left: 406px; top: 765px; width: 1px; height: 240px; background: #c9c9cc; }
</style>
</head>
<body>
<main class="flyer">
  <svg class="flyer-shapes" viewBox="0 0 1216 1724" preserveAspectRatio="none" aria-hidden="true">
    <defs>
      <linearGradient id="soft-grey" x1="0" y1="0" x2="1" y2="1">
        <stop offset="0" stop-color="#ffffff"/>
        <stop offset="0.6" stop-color="#f3f3f5"/>
        <stop offset="1" stop-color="#e8e8eb"/>
      </linearGradient>
      <linearGradient id="photo-tone" x1="0" y1="0" x2="0" y2="1">
        <stop offset="0" stop-color="#56663f"/>
        <stop offset="0.45" stop-color="#3d4a3a"/>
        <stop offset="1" stop-color="#2a3d7a"/>
      </linearGradient>
    </defs>
    <path d="M1216,830 C1000,900 700,1100 400,1300 C200,1430 60,1560 0,1724 H1216 Z" fill="url(#soft-grey)"/>
    <path d="M0,282 C200,360 420,340 560,220 C650,140 720,50 798,0 H1216 V872 C1140,790 1060,720 995,700 C700,570 300,520 0,430 Z" fill="var(--blue-light)"/>
    <path d="M798,0 H1150 C900,40 760,160 640,260 C500,370 250,400 0,320 V282 C200,360 420,340 560,220 C650,140 720,50 798,0 Z" fill="var(--blue-dark)"/>
    <path d="M0,430 C300,520 700,570 1000,702 C1000,840 890,980 725,1028 C550,1078 350,1040 200,1050 C100,1058 30,1110 0,1180 Z" fill="var(--blue-dark)"/>
    <path role="img" aria-label="Photograph of the trust leader standing outdoors with three smiling pupils in navy school blazers" d="M0,430 C300,520 700,570 995,700 C990,830 880,960 720,1010 C550,1060 350,1020 200,1030 C100,1040 30,1100 0,1170 Z" fill="url(#photo-tone)"/>
    <path d="M623,1724 C670,1540 830,1460 1000,1430 C1130,1405 1200,1360 1216,1330 V1724 Z" fill="var(--blue-light)"/>
    <path d="M690,1724 C730,1580 860,1500 1010,1470 C1140,1440 1205,1380 1216,1247 V1724 Z" fill="var(--blue-dark)"/>
    <path d="M740,1724 C780,1620 880,1550 1030,1520 C1140,1495 1200,1450 1216,1390 V1724 Z" fill="var(--white)"/>
  </svg>

  <header class="brand">
    <span class="brand-dot"></span>
    <span class="brand-name">Harbourline<br>Learning<br>Trust</span>
  </header>

  <div class="tag tag--light" style="left:644px; top:169px; width:116px;">Our Vision</div>
  <div class="vision" style="top:202px;">
    <p class="vision-lead">We have one core purpose:</p>
    <p class="vision-copy">To have the biggest positive impact in the varied communities we serve<br>through ensuring top drawer education for our learners.</p>
  </div>

  <div class="tag tag--light" style="left:443px; top:272px; width:317px;">How do we ensure this across our trust?</div>
  <div class="vision" style="top:304px;">
    <p class="vision-lead">In all we do we are:</p>
    <ul class="vision-list">
      <li>Ethical to the core, ensuring that education is always front and centre</li>
      <li>Futures focused system leaders – never simply followers</li>
      <li>Collaborative in every endeavour</li>
      <li>Resolutely learner centred.</li>
    </ul>
  </div>

  <h2 class="photo-question" style="font-weight:400;">What does this look like across our trust?</h2>

  <section>
    <div class="tag tag--solid" style="left:651px; top:684px; width:103px; text-align:right; padding-right:2px;">Education</div>
    <p class="pillar-intro" style="right:38px; top:718px;">We are:</p>
    <ul class="pillar-list pillar-list--right" style="top:735px;">
      <li>Ruthlessly ambitious for all who learn and work with us</li>
      <li>Unwaveringly inclusive – determined on eradicating barriers to educational success</li>
      <li>Committed to excellent teaching</li>
      <li>Determined upon academic excellence for all in our communities</li>
      <li>Compassionate, ethical and caring advocates for all in our communities</li>
      <li>Outwardly facing and globally conscious</li>
    </ul>
  </section>

  <div class="column-rule"></div>

  <section>
    <div class="tag tag--solid" style="left:34px; top:778px; width:110px; padding-left:7px;">Operations</div>
    <p class="pillar-intro" style="left:34px; top:810px;">We are:</p>
    <ul class="pillar-list pillar-list--left" style="top:826px;">
      <li>Committed to the very best people development and empowerment</li>
      <li>Determined to shout loudly and share proudly our successes</li>
      <li>The best professional and technical experts (supporting education) in the sector</li>
      <li>Committed to the very best understanding and management of risk</li>
    </ul>
  </section>

  <section>
    <div class="tag tag--solid" style="left:34px; top:962px; width:110px; padding-left:7px;">Financial</div>
    <p class="pillar-intro" style="left:34px; top:994px;">We are:</p>
    <ul class="pillar-list pillar-list--left" style="top:1012px;">
      <li>Providing the best possible public service for the best possible value</li>
      <li>Determined to supplement our public income with shrewd income generation</li>
      <li>Building financially sustainable models of educational improvement in our communities</li>
      <li>Demonstrably efficient in all we do</li>
    </ul>
  </section>
</main>
</body>
</html>
```